Craft Flavoured Beer Family Extension Desing

We are a Canadian craft brewery looking for the design of a new line of beer we wish to launch within an existing family of products. Our beers are high craft beers that retail for a significant price. Example, 4.49$ for 500 mL vs. 1.49$ for a 500 mL Valdermost.

The line of beer that is being designed here is for a craft flavoured beer line targeted to women. This will be light tasting beers with light fruit flavors targeted to consumers who like beer but are not ready for the strong IPA which are generally found in the craft beer offerings.

The Marisette line, which is the name of this new product, is a ''cousin'' of the existing Gaston-Ferrand Line (more info below).

Target Market(s)

60% Females 40% Males - 21 to 40 years old

Industry/Entity Type

Brewery

Requirements
Must have
• The products will be an INDIRECT family/line extension of the Gaston-Ferrand line of products (design attached). There needs to be some similarities, but it cannot be too close. There are 3 main features on the Gaston-Ferrand label (attached) : (1) the font used for the Logo; (2) the shape of the label; (3) the motif printed on the label.
• The shape of the label must be different than the current shape.
• However, the font of the logo (Gaston-Ferrand) can be the same and the motif printed on the label can be used. Using one of these elements is sufficient to link this new brand with the Gaston-Ferrand brand.
• The name of the product will be MARISETTE
Nice to have
• The bottle, the size, the ABV will be different than for the Gaston-Ferrand beers.
• There will be 3 flavours initially : Blueberry, Grapefruit and Raspberry.
• There needs to be a back label, but if you design, you can use the exact same information as there is currently.
Should not have
• We don't want any fruit pictures or designs on the labels.

```html
<!DOCTYPE html>
<html lang="fr">
<head>
<meta charset="utf-8">
<title>Marisette – Craft Beer Labels</title>
<link rel="stylesheet" href="https://fonts.googleapis.com/css2?family=Bebas+Neue&family=Oswald:wght@400;600&family=Libre+Baskerville&display=swap">
<style>
  :root {
    --page: #ffffff;
    --label: #0c0c0c;
    --ink: #f4f4f2;
    --ink-soft: #bdbdbd;
    --raspberry: #9b2f70;
    --raspberry-arc: #a84a80;
    --grapefruit: #ef8b3d;
    --grapefruit-arc: #e98a45;
    --blackberry: #6c6aa2;
    --blackberry-arc: #7a79a8;
  }
  * { box-sizing: border-box; margin: 0; padding: 0; }
  html, body { width: 1200px; height: 1000px; overflow: hidden; background: var(--page); }
  .canvas { position: relative; width: 1200px; height: 1000px; background: var(--page); }

  .label {
    position: absolute; top: 515px; width: 245px; height: 355px;
    background: var(--label); color: var(--ink); text-align: center;
  }
  .label--raspberry { left: 185px; --accent: var(--raspberry); --arc: var(--raspberry-arc); }
  .label--grapefruit { left: 476px; --accent: var(--grapefruit); --arc: var(--grapefruit-arc); }
  .label--blackberry { left: 761px; --accent: var(--blackberry); --arc: var(--blackberry-arc); }

  .label__brewery { position: absolute; top: 12px; left: 0; width: 245px; height: 50px; }
  .label__brewery text {
    font-family: "Libre Baskerville", serif; font-size: 11.5px; letter-spacing: 1.4px;
    fill: var(--arc);
  }

  .label__ornament {
    position: absolute; left: 50%; transform: translateX(-50%);
    background: radial-gradient(ellipse at center, rgba(230,230,230,0.55) 0%, rgba(120,120,120,0.25) 55%, rgba(12,12,12,0) 80%);
  }
  .label__ornament--top { top: 48px; width: 170px; height: 80px; }
  .label__ornament--bottom { top: 276px; width: 135px; height: 64px; }

  .label__name {
    position: absolute; top: 128px; left: 0; width: 100%;
    font-family: "Bebas Neue", sans-serif; font-size: 66px; line-height: 66px;
    letter-spacing: 1px; color: var(--ink);
  }

  .label__flavour {
    position: absolute; top: 202px; left: 12px; width: 221px; height: 27px;
    background: var(--accent); color: #fff;
    font-family: "Oswald", sans-serif; font-weight: 600; font-size: 14.5px;
    line-height: 27px; letter-spacing: 0.6px;
  }

  .label__origin {
    position: absolute; top: 235px; left: 0; width: 100%;
    font-family: "Libre Baskerville", serif; font-size: 9.5px; letter-spacing: 1.8px;
    color: var(--ink-soft);
  }
  .label__origin .dot { display: inline-block; width: 4px; height: 4px; background: var(--ink-soft); border-radius: 50%; vertical-align: middle; margin: 0 6px; }

  .label__volume {
    position: absolute; top: 252px; left: 0; width: 100%;
    font-family: "Oswald", sans-serif; font-weight: 400; font-size: 14px; line-height: 20px;
    color: var(--ink);
  }
  .label__volume .divider { display: inline-block; width: 2px; height: 14px; background: var(--ink); vertical-align: -2px; margin: 0 8px; }
</style>
</head>
<body>
<main class="canvas">

  <section class="label label--raspberry">
    <svg class="label__brewery" viewBox="0 0 245 50" aria-hidden="false">
      <path id="arc-raspberry" d="M28 46 Q122 10 217 46" fill="none"/>
      <text><textPath href="#arc-raspberry" startOffset="50%" text-anchor="middle">· BRASSERIE DEUX RIVES ·</textPath></text>
    </svg>
    <div class="label__ornament label__ornament--top" role="img" aria-label="Ornamental scroll motif above the name"></div>
    <h2 class="label__name">MARISETTE</h2>
    <p class="label__flavour">RASPBERRY CRAFT BEER</p>
    <p class="label__origin"><span class="dot"></span>BRASSÉE AU QUÉBEC<span class="dot"></span></p>
    <p class="label__volume">500 ML<span class="divider"></span>ALC. 5% VOL</p>
    <div class="label__ornament label__ornament--bottom" role="img" aria-label="Ornamental heart-shaped scroll motif"></div>
  </section>

  <section class="label label--grapefruit">
    <svg class="label__brewery" viewBox="0 0 245 50">
      <path id="arc-grapefruit" d="M28 46 Q122 10 217 46" fill="none"/>
      <text><textPath href="#arc-grapefruit" startOffset="50%" text-anchor="middle">· BRASSERIE DEUX RIVES ·</textPath></text>
    </svg>
    <div class="label__ornament label__ornament--top" role="img" aria-label="Ornamental scroll motif above the name"></div>
    <h2 class="label__name">MARISETTE</h2>
    <p class="label__flavour">GRAPEFRUIT CRAFT BEER</p>
    <p class="label__origin"><span class="dot"></span>BRASSÉE AU QUÉBEC<span class="dot"></span></p>
    <p class="label__volume">500 ML<span class="divider"></span>ALC. 5% VOL</p>
    <div class="label__ornament label__ornament--bottom" role="img" aria-label="Ornamental heart-shaped scroll motif"></div>
  </section>

  <section class="label label--blackberry">
    <svg class="label__brewery" viewBox="0 0 245 50">
      <path id="arc-blackberry" d="M28 46 Q122 10 217 46" fill="none"/>
      <text><textPath href="#arc-blackberry" startOffset="50%" text-anchor="middle">· BRASSERIE DEUX RIVES ·</textPath></text>
    </svg>
    <div class="label__ornament label__ornament--top" role="img" aria-label="Ornamental scroll motif above the name"></div>
    <h2 class="label__name">MARISETTE</h2>
    <p class="label__flavour">BLACKBERRY CRAFT BEER</p>
    <p class="label__origin"><span class="dot"></span>BRASSÉE AU QUÉBEC<span class="dot"></span></p>
    <p class="label__volume">500 ML<span class="divider"></span>ALC. 5% VOL</p>
    <div class="label__ornament label__ornament--bottom" role="img" aria-label="Ornamental heart-shaped scroll motif"></div>
  </section>

</main>
</body>
</html>
```